Re-work our letterhead and create a matching cover page for our LK account

We need a new letterhead to reflect our new social media branding which contains the words Wealth Retirement & Aged Care underneath the name of the company Barrowfield Financial Services Pty Ltd. We need this logo to be able to be used as a Cover page (in .png) for our Linkora account. Colours and format to be derived from files attached.

```html
<!DOCTYPE html>
<html lang="en">
<head>
<meta charset="utf-8">
<title>Barrowfield Financial Services – Letterhead</title>
<link href="https://fonts.googleapis.com/css2?family=Arimo:wght@400;700&display=swap" rel="stylesheet">
<style>
  :root {
    --backdrop: #d9d9d9;
    --paper: #ffffff;
    --ink: #1e1e1e;
    --ink-soft: #333333;
    --muted: #8a8a8a;
    --gold: #e2a527;
    --charcoal: #231f20;
  }
  * { box-sizing: border-box; margin: 0; padding: 0; }
  html, body { width: 1200px; height: 1159px; overflow: hidden; }
  body {
    background: var(--backdrop);
    font-family: "Arimo", Arial, sans-serif;
    color: var(--ink);
    position: relative;
  }
  .letterhead {
    position: absolute;
    left: 204px; top: 20px;
    width: 792px; height: 1120px;
    background: var(--paper);
    box-shadow: 0 6px 24px rgba(0,0,0,.18);
    overflow: hidden;
  }
  .masthead {
    position: absolute; left: 48px; right: 40px; top: 36px; height: 136px;
    border-bottom: 3px solid var(--ink);
    display: flex; align-items: flex-end; justify-content: space-between;
    padding-bottom: 18px;
  }
  .brand { display: flex; flex-direction: column; gap: 4px; }
  .brand-row { display: flex; align-items: center; gap: 10px; }
  .brand-name { font-weight: 700; font-size: 48px; letter-spacing: -1.5px; color: var(--ink); line-height: 1; }
  .brand-mark { width: 16px; height: 16px; background: var(--gold); }
  .brand-tagline { font-size: 15px; font-weight: 700; color: var(--muted); line-height: 1.1; padding-left: 4px; }
  .contacts { display: flex; align-items: stretch; font-size: 12px; line-height: 1.35; color: var(--ink-soft); font-style: normal; padding-bottom: 22px; }
  .contact-block { padding: 0 14px; }
  .contact-block + .contact-block { border-left: 1px solid var(--ink-soft); }
  .contact-block:last-child { padding-right: 0; }
  .letter-body {
    position: absolute; left: 140px; width: 540px; top: 270px;
    font-size: 14px; line-height: 1.3; color: var(--ink);
  }
  .letter-body p { margin-bottom: 36px; }
  .disclaimer {
    position: absolute; left: 48px; right: 40px; bottom: 70px;
    font-size: 12px; color: var(--ink-soft); white-space: nowrap;
  }
  .footer-bands { position: absolute; left: 0; bottom: 0; width: 792px; height: 60px; display: block; }
</style>
</head>
<body>
  <main class="letterhead">
    <header class="masthead">
      <div class="brand">
        <div class="brand-row">
          <span class="brand-name">barrowfield</span>
          <span class="brand-mark" aria-hidden="true"></span>
        </div>
        <span class="brand-tagline">wealth retirement aged care</span>
      </div>
      <address class="contacts">
        <div class="contact-block">ACN 410 552 903<br>48 Linden Street<br>Marlow Vic 3612<br>T (03) 5500 0147</div>
        <div class="contact-block">7 Carrow St<br>Ashvale<br>T (03) 9000 2815</div>
        <div class="contact-block">PO Box 318 Marlow<br>Vic 3612 Marlow<br>Vic 3612</div>
      </address>
    </header>

    <section class="letter-body">
      <p>Lorem ipsum dolor sit amet, consectetur adipiscing elit. Donec fringilla neque euismod volutpat cursus. Vestibulum ac pretium orci, consequat elementum velit. Etiam bibendum purus ac augue finibus volutpat. Vestibulum justo nisl.</p>
      <p>Lorem ipsum dolor sit amet, consectetur adipiscing elit. Donec fringilla neque euismod volutpat cursus. Vestibulum ac pretium orci, consequat elementum velit. Etiam bibendum purus ac augue finibus volutpat. Vestibulum justo nisl, gravida aliquet sollicitudin ut, finibus vitae mi. Praesent aliquet scelerisque blandit. Sed id varius lacus, id tristique sem. Fusce et lobortis leo. Aliquam mollis pellentesque magna, condimentum ullamcorper ex ullamcorper non. Morbi ultricies nunc eu tellus dignissim, eget venenatis dolor ullamcorper. Etiam dolor eros, iaculis at ultricies nec, volutpat nec orci. Vivamus tincidunt rutrum sapien, ac porttitor mauris tristique nec.</p>
      <p>Lorem ipsum dolor sit amet, consectetur adipiscing elit. Donec fringilla neque euismod volutpat cursus. Vestibulum ac pretium orci, consequat elementum velit. Etiam bibendum purus ac augue finibus volutpat. Vestibulum justo nisl, gravida aliquet sollicitudin ut, finibus vitae mi. Praesent aliquet scelerisque blandit. Sed id varius lacus, id tristique sem. Fusce et lobortis leo. Aliquam mollis pellentesque magna, condimentum ullamcorper ex ullamcorper non. Morbi ultricies nunc eu tellus dignissim, eget venenatis dolor ullamcorper. Etiam dolor eros, iaculis at ultricies nec, volutpat nec orci. Vivamus tincidunt rutrum sapien, ac porttitor mauris tristique nec.</p>
      <p>Lorem ipsum dolor sit amet, consectetur adipiscing elit. Donec fringilla neque euismod volutpat cursus. Vestibulum ac pretium orci, consequat elementum velit. Etiam bibendum purus ac augue finibus volutpat. Vestibulum justo nisl.</p>
    </section>

    <p class="disclaimer">Barrowfield Financial Services Pty Ltd is a Corporate Authorised Representative of Keystone Advice Pty Ltd AFSL 500913</p>

    <svg class="footer-bands" viewBox="0 0 792 60" aria-hidden="true">
      <polygon points="0,34 540,34 568,60 0,60" fill="var(--gold)"/>
      <polygon points="556,14 792,0 792,18 590,34" fill="var(--charcoal)"/>
    </svg>
  </main>
</body>
</html>
```